Cycling Group adventures - weekly cycling with Ridewell Federation Coach for health and fitness

An A3 poster, like a flyer for information about a new cycling group. Lots of info on the poster so designed to be read close up and not needing to get attention from a long way off. All the info, yes there is a lot, is on the Word document attached. My colours are blue RGB 83, 108, 255 and orange 226, 83, 3.
There are three sections of info on the Word document the first is the most important.
The market is affluent and middle-aged.
So nothing wild or shouty. Nice, sophisticated, peaceful designs.
Photos really are background to the words. (I think I've accidentally downloaded some twice although I thought they were deleted.)

Industry/Entity Type

Health And Wellness

Font styles to use
Sans Serif

Requirements
Must have
• Clear font
Should not have
• Jazzy colours, lots of bubbles, flashy things or anything that looks like an advert for cheap jewellery/perfume/used cars.

```html
<!DOCTYPE html>
<html lang="en">
<head>
<meta charset="utf-8">
<title>Cycling with Roundleaf Riders</title>
<link rel="stylesheet" href="https://fonts.googleapis.com/css2?family=Open+Sans:wght@400;600;700&display=swap">
<style>
:root{
  --blue:#536cff;
  --orange:#e25303;
  --row:#eceef3;
  --ink:#3b3f4a;
  --muted:#6b7080;
  --grass-dark:#4f8a22;
  --grass-light:#9fd057;
  --white:#ffffff;
}
*{box-sizing:border-box;margin:0;padding:0}
html,body{width:887px;height:1200px;overflow:hidden;background:var(--white)}
body{font-family:"Open Sans",Arial,sans-serif;color:var(--ink);position:relative}
.photo-grid{position:absolute;top:0;left:0;width:887px;height:330px;display:grid;grid-template-columns:1.5fr 1fr 1fr;grid-template-rows:1fr 1fr;gap:6px;background:var(--white)}
.photo{background:linear-gradient(160deg,#a9c4a0,#6f8f6a 55%,#8c9299)}
.photo.tall{grid-row:span 2;background:linear-gradient(170deg,#b8ccd9,#7f9a7a 60%,#5e6b62)}
.photo.alt{background:linear-gradient(150deg,#c5d3e0,#8aa58c 50%,#6d7469)}
.photo.warm{background:linear-gradient(150deg,#d7d0c2,#9fae8c 55%,#707a6d)}
.info{position:absolute;top:352px;left:40px;width:807px}
.info-row{display:grid;grid-template-columns:120px 1fr;gap:6px;margin-bottom:6px}
.label{background:var(--blue);color:var(--white);font-weight:600;font-size:13px;padding:10px 12px;display:flex;align-items:center}
.value{background:var(--row);font-size:12px;padding:10px 14px;display:flex;align-items:center;gap:10px}
.value .slot{background:var(--white);padding:2px 22px}
.coach-row .value{align-items:flex-start;font-size:11px;line-height:1.5;padding-right:150px;position:relative;min-height:96px}
.coach-photo{position:absolute;right:14px;top:-110px;width:120px;height:160px;background:linear-gradient(170deg,#e6ecf2,#c98a5e 60%,#536cff)}
.qa{position:absolute;top:745px;left:40px;width:807px;display:grid;grid-template-columns:1fr 1fr;gap:14px}
.qa-item{display:grid;grid-template-columns:70px 1fr;gap:6px;margin-bottom:6px}
.q{background:var(--blue);color:var(--white);font-size:10px;font-weight:600;padding:6px 8px;line-height:1.3}
.a{background:var(--row);font-size:9.5px;line-height:1.4;padding:6px 8px}
.options{position:absolute;top:1005px;left:40px;width:807px;border:1px solid #c9ccd6;padding:10px 14px;display:grid;grid-template-columns:1fr 1fr;column-gap:24px}
.options h2{grid-column:span 2;color:var(--orange);font-size:13px;font-weight:700;margin-bottom:6px}
.options p{font-size:9.5px;line-height:1.45;margin-bottom:4px;color:var(--muted)}
.footer{position:absolute;left:0;bottom:0;width:887px;height:82px;background:linear-gradient(180deg,var(--grass-light),var(--grass-dark))}
.brand{position:absolute;right:40px;bottom:24px;display:flex;align-items:center;gap:10px;font-size:30px;font-weight:700;color:var(--white)}
.brand .dot{width:22px;height:22px;border-radius:50%;background:var(--orange)}
</style>
</head>
<body>
<section class="photo-grid">
  <div class="photo tall" role="img" aria-label="Group of cyclists riding along a tree-lined road"></div>
  <div class="photo alt" role="img" aria-label="Cyclists resting by the roadside"></div>
  <div class="photo warm" role="img" aria-label="Riders in cycling kit posing together"></div>
  <div class="photo" role="img" aria-label="Cyclists on a quiet country road"></div>
  <div class="photo alt" role="img" aria-label="Riders with bikes near a park"></div>
</section>

<section class="info">
  <div class="info-row"><div class="label">What?</div><div class="value">Cycling with Roundleaf Riders – www.roundleafriders.com.au&nbsp; 0400 123 456</div></div>
  <div class="info-row"><div class="label">Where?</div><div class="value"></div></div>
  <div class="info-row"><div class="label">When?</div><div class="value">Day: <span class="slot">&nbsp;</span> Date: <span class="slot">&nbsp;</span> Weekly 60 min (or six sessions for 5 weeks).</div></div>
  <div class="info-row"><div class="label">Who?</div><div class="value">Up to 7 participants</div></div>
  <div class="info-row"><div class="label">Booking essential?</div><div class="value">Yes, for purposes of insurance.</div></div>
  <div class="info-row coach-row"><div class="label">Who coaches it?</div><div class="value">Daniel Hart, Ridewell Federation accredited coach, a coach of the state junior program, ride leader of Ridewell Federation's ride program and past state rider. He has an exercise science degree, has trained with a national team and writes about cycling for health. Daniel can ride with all abilities and loves to share the joy of cycling.<div class="coach-photo" role="img" aria-label="Portrait of the coach in cycling kit"></div></div></div>
</section>

<section class="qa">
  <div>
    <div class="qa-item"><div class="q">Women and men?</div><div class="a">Often both, though this time of day commonly suits mostly women riders.</div></div>
    <div class="qa-item"><div class="q">Is it competitive?</div><div class="a">No, this is not a race.</div></div>
    <div class="qa-item"><div class="q">Might I get left behind?</div><div class="a">No, we ride together and regroup often so nobody rides alone.</div></div>
    <div class="qa-item"><div class="q">Clothing?</div><div class="a">Close fitting sporting clothing is fine if you are not a racer. Padded shorts help, and bring a light jacket for cool mornings.</div></div>
    <div class="qa-item"><div class="q">Bike?</div><div class="a">All types welcome. If you are on a road or hybrid bike, we will help check it is safe before the first ride.</div></div>
  </div>
  <div>
    <div class="qa-item"><div class="q">Ability level?</div><div class="a">Aimed at people who can ride a bike, including those not confident yet. We build skills slowly so you can ride further with ease.</div></div>
    <div class="qa-item"><div class="q">Will it be a social ability?</div><div class="a">Always. A coffee stop is part of every ride for those who want to join.</div></div>
    <div class="qa-item"><div class="q">How much?</div><div class="a">$149 for the 5 weeks.</div></div>
    <div class="qa-item"><div class="q">Do we have coffee afterwards?</div><div class="a">If you like! It is a relaxed way to finish, and the group usually stays for a chat.</div></div>
    <div class="qa-item"><div class="q">How vital?</div><div class="a">Booking by phone is the best way.</div></div>
  </div>
</section>

<section class="options">
  <h2>Some Other Options</h2>
  <p>"I'd like a different day and time"<br>Give me a ring and we can plan a time.</p>
  <p>One-on-one sessions are also available.<br>This is a good option to try before a group.</p>
  <p>"I ride regularly, can do 80km or more and want to be quicker."<br>Ask about our skills and speed sessions.</p>
  <p>I also present rides from Ridewell Federation, see the website or call me for details.</p>
</section>

<footer class="footer" role="img" aria-label="Strip of green grass">
  <div class="brand"><span class="dot"></span>Roundleaf Riders</div>
</footer>
</body>
</html>
```